CD Cover (EDM, Tropical, Urban) Home and biscuit CD (electronic music tropica, urban, ethnic)

We seek a tropical design, ethnic, wild, colorful, etc ... for an album of electronic music with those same characteristics. Attached indicative examples of what we would like. The music is similar to that of the examples, not only the cover we seek. The title of the CD is as follows: TOLUVA RESONARIOS PRESENTS DPK Thanks! -------------------------------- Looking for a tropical, ethnic, colorful design ... for a music CD. We attached examples of what kind of design we want. The music of esta CD is similar to the examples, not only in the cover, Also the music. The title of the CD (the only text) is: TOLUVA RESONARIOS PRESENTS DPK Thanks! ------------------------------

Target Market(s)

Young audience, consumer electronic music / Young people, music EDM Consumers

Industry/Entity Type

Music Download

Font styles to use
Serif

Requirements
Must have
• To resemble any of the accompanying examples, serve. / Like the attached examples.
Nice to have

```html
<!DOCTYPE html>
<html lang="es">
<head>
<meta charset="utf-8">
<title>Toluva Resonarios presenta DPK</title>
<link rel="stylesheet" href="https://fonts.googleapis.com/css2?family=Passion+One:wght@700&display=swap">
<style>
  :root {
    --backdrop: #e0578b;
    --teal: #22968f;
    --teal-light: #3dbcb4;
    --leaf-green: #9cbf4c;
    --flower-pink: #e23a77;
    --paper: #f4f4f4;
    --ink: #161616;
  }
  html, body {
    margin: 0;
    padding: 0;
    width: 1200px;
    height: 676px;
    overflow: hidden;
    background: var(--backdrop);
  }
  .stage {
    display: block;
    width: 1200px;
    height: 676px;
  }
  .label-line,
  .label-small,
  .album-title {
    font-family: "Passion One", sans-serif;
    font-weight: 700;
    fill: var(--ink);
  }
  .label-small {
    letter-spacing: 1px;
  }
</style>
</head>
<body>
<svg class="stage" viewBox="0 0 1200 676" xmlns="http://www.w3.org/2000/svg">
  <defs>
    <linearGradient id="jungle" x1="0" y1="0" x2="1" y2="1">
      <stop offset="0" stop-color="var(--teal-light)"/>
      <stop offset="0.3" stop-color="var(--leaf-green)"/>
      <stop offset="0.5" stop-color="var(--teal)"/>
      <stop offset="0.72" stop-color="var(--flower-pink)"/>
      <stop offset="1" stop-color="var(--teal-light)"/>
    </linearGradient>
  </defs>

  <rect class="backdrop" width="1200" height="676" fill="var(--backdrop)"/>

  <!-- Disc -->
  <g class="disc">
    <circle class="disc-artwork" cx="840" cy="334" r="258" fill="url(#jungle)"
            role="img" aria-label="Tropical leaves and pink hibiscus illustration around the disc rim"/>
    <circle class="disc-label" cx="840" cy="334" r="216" fill="var(--paper)"/>
    <circle class="disc-ring" cx="840" cy="334" r="207" fill="none" stroke="var(--teal)" stroke-width="3"/>
    <text class="label-line" x="850" y="199" font-size="14" text-anchor="middle">TOLUVA</text>
    <text class="label-line" x="850" y="213" font-size="14" text-anchor="middle">RESONARIOS</text>
    <text class="label-small" x="850" y="225" font-size="7" text-anchor="middle">PRESENTA</text>
    <text class="album-title" x="850" y="420" font-size="200" text-anchor="middle"
          textLength="340" lengthAdjust="spacingAndGlyphs">DPK</text>
  </g>

  <!-- Sleeve -->
  <g class="sleeve">
    <rect class="sleeve-artwork" x="82" y="58" width="566" height="548" fill="url(#jungle)"
          role="img" aria-label="Tropical jungle illustration with monstera leaves, ferns and pink hibiscus flowers"/>
    <rect class="title-panel" x="242" y="212" width="242" height="242" fill="var(--paper)"/>
    <text class="label-line" x="363" y="268" font-size="24" text-anchor="middle">TOLUVA</text>
    <text class="label-line" x="363" y="292" font-size="24" text-anchor="middle">RESONARIOS</text>
    <text class="label-small" x="363" y="308" font-size="11" text-anchor="middle">PRESENTA</text>
    <text class="album-title" x="363" y="410" font-size="96" text-anchor="middle"
          textLength="180" lengthAdjust="spacingAndGlyphs">DPK</text>
  </g>
</svg>
</body>
</html>
```